Business card - mobile service

O KiraVox is a mobile family safety service based on tablets and smartphones.
The business card must have:
BASIC INFO
Company Logo
Name
Position / Job Title: Co-founder
Mobile Phone Number: +55 (11) 5830 9172
Land Line: +55 (11) 8761 203945
Email Address: name@kiravox-example.com
Web Site URL: www.kiravox-example.com
PROMOTIONAL INFO
Try KiraVox free Today!
Your personal promo code: qqqq-5839-wwww-4162-9087
Promo code text explanation with the instructions about the trial offer
Updates
Dears,
One more must have: the KiraVox slogan:
Safety

```html
<!DOCTYPE html>
<html lang="en">
<head>
<meta charset="utf-8">
<title>KiraVox – Business Card</title>
<link rel="stylesheet" href="https://fonts.googleapis.com/css2?family=Open+Sans:wght@300;400;700;800&display=swap">
<style>
  :root {
    --brand-blue: #00a0df;
    --brand-yellow: #f9c60f;
    --ink: #1d1d1b;
    --paper: #ffffff;
    --shadow: rgba(0, 0, 0, 0.18);
  }
  * { box-sizing: border-box; margin: 0; padding: 0; }
  html, body {
    width: 1200px; height: 900px; overflow: hidden;
    background: var(--paper);
    font-family: "Open Sans", sans-serif;
    color: var(--ink);
  }
  .stage { position: relative; width: 1200px; height: 900px; }

  .card {
    position: absolute;
    width: 648px; height: 395px;
    border-radius: 40px;
    box-shadow: 4px 6px 8px var(--shadow);
    overflow: hidden;
  }
  .card--back {
    left: 467px; top: 420px;
    background: var(--brand-blue);
    z-index: 1;
  }
  .card--front {
    left: 85px; top: 85px;
    height: 393px; width: 647px;
    background: var(--paper);
    z-index: 2;
  }

  /* Front face */
  .wordmark {
    position: absolute; left: 32px; top: 42px;
    font-size: 76px; font-weight: 800; letter-spacing: -1px;
    color: var(--brand-blue); line-height: 1;
  }
  .slogan {
    position: absolute; left: 175px; top: 135px;
    font-size: 14px; color: var(--ink);
  }
  .contact { position: absolute; left: 355px; top: 174px; }
  .contact__name { font-size: 23px; font-weight: 700; line-height: 1.2; }
  .contact__role { font-size: 16px; margin-top: 2px; }
  .contact__phones { margin-top: 18px; font-size: 16px; line-height: 24px; }
  .contact__phones dt { font-weight: 700; float: left; clear: left; width: 85px; }
  .contact__phones dd { margin-left: 85px; }
  .contact__web { margin-top: 22px; font-size: 16px; line-height: 24px; list-style: none; }
  .contact__web b { display: inline-block; width: 20px; text-align: center; }

  /* Back face */
  .back__mark { position: absolute; left: 0; top: 0; }
  .promo {
    position: absolute; left: 295px; top: 112px;
    color: var(--paper); font-size: 18px; font-weight: 300; line-height: 26px;
  }
  .promo p + p { margin-top: 24px; }
</style>
</head>
<body>
<main class="stage">
  <section class="card card--back" aria-label="Promotional side">
    <svg class="back__mark" width="648" height="395" viewBox="0 0 648 395" aria-hidden="true">
      <circle cx="96" cy="308" r="92" fill="var(--brand-yellow)"/>
    </svg>
    <div class="promo">
      <p>Try KiraVox free Today!</p>
      <p>Your personal promo code<br>qqqq-5839-wwww-4162-9087</p>
      <p>Promo code text explanation with<br>the instructions about the trial offer</p>
    </div>
  </section>

  <section class="card card--front" aria-label="Contact side">
    <div class="wordmark">KiraVox</div>
    <div class="slogan">Your Family Safety Service</div>
    <div class="contact">
      <h1 class="contact__name">Rafael Mendes</h1>
      <p class="contact__role">Co-founder</p>
      <dl class="contact__phones">
        <dt>Land Line</dt><dd>+55 (11) 8761 203945</dd>
        <dt>Mobile</dt><dd>+55 (11) 5830 9172</dd>
      </dl>
      <ul class="contact__web">
        <li><b>e</b> name@kiravox-example.com</li>
        <li><b>w</b> www.kiravox-example.com</li>
      </ul>
    </div>
  </section>
</main>
</body>
</html>
```